依頼詳細
PCとスマホデザインの両方納品をいただきますが、
まずはデザインイメージが確認しやすいPCページのみの提案をお願いします。
スマホページは当選者に納品時にお願いしたいと思います。
スマホサイズは横幅750pxのサイズで作成してください。

レスポンシブウェブデザインを意識したデザインでお願いします。

デザインに関しては、添付してあるデザインレイアウト設計シートを基にお願いします。
参考サイトのURLはデザインレイアウト設計シートに記載してあります。

画像データについては、フリー素材から流用してイメージ画像に当て込んでください。

足りない場合は、一旦他のサイトの写真をサンプルとして入れてください。
また、購入が必要な写真などを利用した場合、価格とサイト名を教えてください。
ページ数
1ページ
希望イメージ
シンプル 複雑
単色 カラフル
暗い 明るい
日常 高級
遊び心 厳粛
未来的 伝統的
女性的 男性的
納品ファイル
• イラストレーター形式 (.ai)
• フォトショップ形式 (.psd)
• PNG形式 (.png)
補足説明
上記のいずれか1つ(アウトラインありとなしの2つ)と高解像度JPGを納品お願いします。
■ 選んだ理由

クライアント様より選定いただきました。
一番イメージに近いものでした

■ 提案者全員のお礼・コメント

ご提案ありがとうございました。
また機会がありましたら是非お願いします。

```html
<!DOCTYPE html>
<html lang="ja">
<head>
<meta charset="utf-8">
<title>柏木製作所 | 物流と倉庫の収納・保管</title>
<link href="https://fonts.googleapis.com/css2?family=Noto+Sans+JP:wght@400;500;700&family=Roboto:wght@400;700&display=swap" rel="stylesheet">
<style>
:root{
  --red:#d0191c;
  --ink:#222;
  --muted:#777;
  --line:#dcdcdc;
  --footer:#3b3b3b;
  --band-a:#dfe8f4;
  --band-b:#c5d3e6;
  --shop-yellow:#fff3b8;
  --shop-pink:#ffe8e8;
  --white:#fff;
}
*{box-sizing:border-box;margin:0;padding:0}
html,body{width:1200px;height:2172px;overflow:hidden;background:var(--white)}
body{font-family:"Noto Sans JP",sans-serif;color:var(--ink);position:relative}
.abs{position:absolute}

/* header & hero */
.hero{left:0;top:0;width:1200px;height:672px;
  background:linear-gradient(180deg,rgba(0,0,0,.55),rgba(0,0,0,.25) 40%,rgba(0,0,0,.45)),
  linear-gradient(90deg,#5a1a14,#9a3224 25%,#6b5e58 50%,#a23a2a 75%,#4a1712)}
.brand{left:24px;top:28px;font-family:"Roboto",sans-serif;font-weight:700;font-size:20px;letter-spacing:1px;color:var(--white)}
.nav{right:24px;top:32px;display:flex;gap:22px;list-style:none;font-size:11px;color:var(--white)}
.hero-copy{left:0;width:1200px;top:262px;text-align:center;color:var(--white);font-weight:700;font-size:34px;line-height:1.75;letter-spacing:3px;text-shadow:0 2px 8px rgba(0,0,0,.4)}

/* about */
.about-photo{left:120px;top:732px;width:470px;height:380px;background:linear-gradient(135deg,#f3c78c,#c8442c 45%,#7b2a20 80%,#3e1e1a)}
.about-body{left:630px;top:752px;width:450px}
.sec-title{font-size:22px;font-weight:700;letter-spacing:1px}
.sec-en{font-family:"Roboto",sans-serif;font-size:11px;font-weight:700;color:var(--red);letter-spacing:1px;margin-top:6px}
.about-lead{margin-top:26px;padding-left:14px;border-left:3px solid var(--red);font-size:17px;font-weight:700;line-height:1.7}
.about-text{margin-top:26px;font-size:12px;line-height:2;color:var(--muted)}
.btn{display:flex;align-items:center;justify-content:space-between;width:150px;height:38px;padding:0 14px 0 22px;background:var(--red);color:var(--white);font-size:12px;font-weight:500}
.about-btn{left:690px;top:1020px}

/* service band */
.band{left:0;top:1172px;width:1200px;height:330px;background:linear-gradient(120deg,var(--band-a),var(--band-b) 60%,var(--band-a))}
.card{width:360px;height:200px;top:1237px;display:flex;align-items:center;justify-content:center}
.card-a{left:228px;background:linear-gradient(135deg,#5d2a22,#a44a36 50%,#3a2622)}
.card-b{left:612px;background:linear-gradient(135deg,#3c3f52,#8a6a5a 50%,#b24a3a)}
.card-label{width:120px;height:50px;border:1px solid rgba(255,255,255,.8);background:rgba(0,0,0,.35);color:var(--white);font-size:14px;font-weight:500;display:flex;align-items:center;justify-content:center;letter-spacing:1px}

/* news */
.news-head{left:228px;top:1562px}
.news-list{left:452px;top:1578px;width:520px;list-style:none}
.news-list li{display:flex;gap:28px;height:38px;align-items:center;border-bottom:1px solid var(--line);font-size:12px;color:var(--muted)}
.news-list time{font-family:"Roboto",sans-serif;color:var(--red);font-weight:700;width:70px}
.news-btn{left:228px;top:1722px}

/* shops */
.shop{top:1852px;width:344px;height:120px;display:flex;align-items:center;gap:22px;padding:0 22px}
.shop-official{left:248px;background:var(--shop-yellow);border:2px solid #f0d96a}
.shop-mall{left:620px;background:var(--shop-pink);border:2px solid var(--red)}
.shop-art{width:100px;height:80px;background:linear-gradient(135deg,#ffe27a,#f4b24a)}
.shop-mall .shop-art{background:linear-gradient(135deg,#ffd0d0,#e45a5a)}
.shop-name{font-family:"Roboto",sans-serif;font-weight:700;font-size:15px;letter-spacing:1px;line-height:1.5}
.shop-name span{display:block;font-family:"Noto Sans JP",sans-serif;font-size:17px}
.shop-mall .shop-name{color:var(--red)}

/* footer */
.footer{left:0;top:2028px;width:1200px;height:144px;background:var(--footer);color:var(--white)}
.f-brand{left:228px;top:26px;font-family:"Roboto",sans-serif;font-weight:700;font-size:17px;letter-spacing:1px}
.f-address{left:228px;top:58px;font-size:10px;line-height:1.8;color:#cfcfcf}
.f-nav{left:612px;top:28px;display:grid;grid-template-columns:repeat(5,auto);column-gap:26px;row-gap:14px;list-style:none;font-size:10px;color:#e8e8e8}
.f-copy{left:0;width:1200px;bottom:10px;text-align:center;font-size:9px;color:#aaa;font-family:"Roboto",sans-serif}
</style>
</head>
<body>

<header>
  <div class="abs hero" role="img" aria-label="倉庫の高い棚と通路を走るフォークリフトの写真"></div>
  <div class="abs brand">KASHIWAGI</div>
  <ul class="abs nav">
    <li>会社概要</li><li>製品情報</li><li>導入事例</li><li>お知らせ</li><li>採用情報</li><li>お問い合わせ</li>
  </ul>
  <h1 class="abs hero-copy">物流と倉庫の収納・保管を<br>安全かつ効率的に</h1>
</header>

<section>
  <div class="abs about-photo" role="img" aria-label="夕日が差し込む倉庫の棚とフォークリフトの写真"></div>
  <div class="abs about-body">
    <h2 class="sec-title">柏木製作所について</h2>
    <p class="sec-en">ABOUT US</p>
    <p class="about-lead">物流と倉庫の収納・保管の<br>効率化・安全化を提案します</p>
    <p class="about-text">私たちは倉庫用ラックや保管設備の設計から施工まで一貫して手掛けています。現場ごとの課題に寄り添い、限られた空間を最大限に活かす収納をご提案します。安全性と作業効率を両立し、お客様の物流を長く支えるパートナーを目指しています。</p>
  </div>
  <a class="abs btn about-btn">詳細情報<svg width="8" height="10" viewBox="0 0 8 10"><path d="M1 1l5 4-5 4" fill="none" stroke="#fff" stroke-width="1.6"/></svg></a>
</section>

<section>
  <div class="abs band" role="img" aria-label="淡い青色に重ねた倉庫内部の写真"></div>
  <div class="abs card card-a" role="img" aria-label="製品の保管ラックの写真"><span class="card-label">製品情報</span></div>
  <div class="abs card card-b" role="img" aria-label="導入先倉庫の写真"><span class="card-label">導入事例</span></div>
</section>

<section>
  <div class="abs news-head">
    <h2 class="sec-title">お知らせ</h2>
    <p class="sec-en">NEWS</p>
  </div>
  <ul class="abs news-list">
    <li><time>2022.00.00</time>ホームページをリニューアルしました</li>
    <li><time>2022.00.00</time>夏季休業期間のお知らせ</li>
    <li><time>2022.00.00</time>新製品の保管ラックを発売しました</li>
    <li><time>2022.00.00</time>物流展示会に出展いたします</li>
    <li><time>2022.00.00</time>導入事例を追加しました</li>
  </ul>
  <a class="abs btn news-btn">一覧を見る<svg width="8" height="10" viewBox="0 0 8 10"><path d="M1 1l5 4-5 4" fill="none" stroke="#fff" stroke-width="1.6"/></svg></a>
</section>

<section>
  <a class="abs shop shop-official">
    <div class="shop-art" role="img" aria-label="パソコンで買い物をする人物のイラスト"></div>
    <p class="shop-name">KASHIWAGI<span>公式ショップ</span></p>
  </a>
  <a class="abs shop shop-mall">
    <div class="shop-art" role="img" aria-label="ノートパソコンとショッピングカートのイラスト"></div>
    <p class="shop-name">KASHIWAGI<span>モールショップ</span></p>
  </a>
</section>

<footer class="abs footer">
  <div class="abs f-brand">KASHIWAGI</div>
  <p class="abs f-address">〒000-0000 東京都みどり区さくら町1-2-3<br>TEL 00-0000-0000<br>FAX 00-0000-0001</p>
  <ul class="abs f-nav">
    <li>会社概要</li><li>製品情報</li><li>導入事例</li><li>お知らせ</li><li>お問い合わせ</li>
    <li>採用情報</li><li>公式ショップ</li><li>モールショップ</li><li>プライバシー</li><li>サイトマップ</li>
  </ul>
  <p class="abs f-copy">© KASHIWAGI Co., Ltd.</p>
</footer>

</body>
</html>
```